Stationary for Keeping Steady

we are in the process of creating a more professional image for our company Keeping Steady Paramedical Services. We have recently had a new logo and general brochure designed using artpitchhub and have been impressed by the quality of submissions.

We need:
- Letterhead (A4)
- Business Cards
- With compliments slips
- Email stationary

Letterhead information:
Address - 47 Wattlebrook Drive, Fernhollow Vic 3091
Phone - 1800 462 817
email - enquiries@keepsteady.com.au
Internet - www.keepsteady.com.au
ABN - 82 463 915 207
ACN - 264 871 035

Files need to be able to be edited in Illustrator CS2

Business Cards / with compliments slips / email stationary:
Double sided.
One side to have Name, Mobile number, company phone 1800462817, email, internet address

Files need to be able to be edited in Illustrator CS2 (except email stationary)

Our website is www.keepsteady.com.au for more information. Do not base designs on the website as it will eventually be revised.

Target Market(s)

Australian based businesses, government departments and schools. We specialise in corporate customers rather than public first aid course

Industry/Entity Type

Internet

Requirements
Must have
• Where applicable file to be editable in illustrator CS2 to allow future alterations.

```html
<!DOCTYPE html>
<html lang="en">
<head>
<meta charset="utf-8">
<title>Keeping Steady Letterhead</title>
<link href="https://fonts.googleapis.com/css2?family=Arimo:wght@400;700&display=swap" rel="stylesheet">
<style>
:root{
  --backdrop:#a0a1a5;
  --paper:#ffffff;
  --paper-back:#e2e3e5;
  --ink:#111111;
  --muted:#555555;
  --brand-red:#e0433a;
  --rule:#a9a9a9;
  --faint:#ececec;
  --shadow:rgba(0,0,0,.35);
}
*{margin:0;padding:0;box-sizing:border-box}
html,body{width:1200px;height:900px;overflow:hidden}
body{background:var(--backdrop);font-family:'Arimo',Arial,sans-serif;color:var(--ink);position:relative}
.sheet{position:absolute;top:77px;width:520px;height:736px;box-shadow:2px 3px 4px var(--shadow);overflow:hidden}
.sheet--front{left:63px;background:var(--paper)}
.sheet--back{left:624px;background:var(--paper-back)}
.sheet > *{position:absolute}

.fold-mark{left:0;top:246px;width:9px;height:1px;background:#333}
.accent-block{left:335px;top:293px;width:160px;height:160px;background:var(--faint)}

.recipient{left:96px;top:34px;font-size:12px;line-height:14px}
.subject{left:96px;top:166px;font-size:9.5px;line-height:12px}
.greeting{left:96px;top:202px;font-size:9.5px;font-weight:700}
.body-copy{left:96px;top:252px;width:316px;font-size:9px;line-height:11.6px;font-weight:700}
.body-copy p{margin-bottom:11.6px}
.sign-off{left:96px;top:509px;font-size:9px;font-weight:700}
.signatory{left:96px;top:546px;font-size:9px;font-weight:700}

.footer-rule{left:17px;top:641px;width:478px;height:1px;background:var(--rule)}
.brand{left:39px;top:662px;display:flex;align-items:flex-start;gap:7px}
.brand-square{width:14px;height:14px;background:var(--brand-red);margin-top:3px}
.brand-name{color:var(--brand-red);font-size:16px;font-weight:700;line-height:17px}
.brand-name small{display:block;font-size:10px;line-height:12px}
.registration{left:101px;top:703px;font-size:7.5px;color:var(--muted);font-weight:700}
.contact{left:334px;top:665px;font-size:7.8px;line-height:10.3px;color:#333}
.contact b{font-weight:700}

.back-block{left:184px;top:291px;width:160px;height:160px;background:var(--paper)}
.brand--reverse{left:33px;top:641px}
.brand--reverse .brand-square{background:var(--paper)}
.brand--reverse .brand-name{color:var(--paper)}
</style>
</head>
<body>
<section class="sheet sheet--front" aria-label="Letterhead">
  <div class="fold-mark"></div>
  <div class="accent-block"></div>
  <address class="recipient" style="font-style:normal">To:<br>Mr. Henry Maddox<br>Linwood Hospital Reception<br>Harbourview Road<br>Eastmere VIC 3187</address>
  <div class="subject">Re: New AED Technology<br>Date: 08.02.2011</div>
  <div class="greeting">Dear Mr. Henry Maddox,</div>
  <div class="body-copy">
    <p>Archil ipicitio. Ipsuntotae cones sequi temos everit re sum quias eiciet officit asin et qui oditasitis a desed quosten ditatestio. Nequamus pore, quia conseque vere expla nos enist, net incil et la dolor aut iuriame si blabo. Mi, venis ea soluptat.</p>
    <p>Soluptatquam con reritas perspient ius quiduntorpos el eum vel-land iandic tem con cullore quo blaut aditatis illes imincid elitas ex enis et fugit aspitem cum etur?</p>
    <p>Ris ea nectatur solesci aspediam sed maximetur? Rem. Temo velloria con rehendamus exerum facero temque nonsernatem quam, simollam eictotat pliquatem acerion ectur, oditaqui odit venihitas anditiis que voluptatem volore nis ut pre dolo dis ac-caerorepra cust rem veliquassus di dolupta temquia peliquatus, serferu ptatem nos doleserum re nihicae non esto que volorest quodita illaborem ut as reniatur, secae ent fugiam idelend eratquas peroribeatur alia core que non cum endam remposaerspe et omnis mincili</p>
  </div>
  <div class="sign-off">Kind Regards</div>
  <div class="signatory">Daniel Ashcroft</div>
  <div class="footer-rule"></div>
  <div class="brand">
    <span class="brand-square"></span>
    <div class="brand-name">Keeping Steady<small>Paramedical Services Pty Ltd</small></div>
  </div>
  <div class="registration">ABN 82 463 915 207 ACN 264 871 035</div>
  <div class="contact">47 Wattlebrook Drive<br>Fernhollow VIC 3091<br><b>Phone</b> 1800 462 817<br><b>Email</b> enquiries@keepsteady.com.au<br><b>Web</b> www.keepsteady.com.au</div>
</section>

<section class="sheet sheet--back" aria-label="Letterhead reverse">
  <div class="back-block"></div>
  <div class="brand brand--reverse">
    <span class="brand-square"></span>
    <div class="brand-name">Keeping Steady<small>Paramedical Services Pty Ltd</small></div>
  </div>
</section>
</body>
</html>
```